Flaschenetikett für Nahrungsergänzungsmittel
Zielgruppe
Wir betreiben eine Naturheilpraxis für Mensch und Tier.
Neben der Behandlung von Menschen und Tieren soll der Verkauf von Nahrungsergänzungsmitteln ausgebaut werden.
Unsere Zielgruppe sind Verbraucher, die der Naturheilkunde und traditionellen Naturheilmitteln zugewandt sind.
Aufgabenstellung
Entstehen soll ein Flaschenetikett für 'Kolloidales Silber'. Es gibt eine Vorder- und eine Rückseite.
Zukünftig werden verschiedene Produkte bzw. Nahrungsergänzungsmittel zum Verkauf angeboten. Damit ein gewisser Wiedererkennungswert entsteht, sollen die einzelnen Etiketten von der Art gleich/ähnlich sein und sich nur durch bestimmte Formen oder Farben unterscheiden.
Unser bestehendes Logo finden sie anbei.
Hier der Link zur verwendeten 1000ml Braunglasflasche.
https://www.gebindor.de/flaschen/glasflaschen/meplatflasche/7312/1000-ml-meplatflasche-glas-braun-pp-28-meplat
Wünschenswert wäre, wenn das Etikett auf eine 500ml Flasche skaliert werden könnte.
Hier der Link zur verwendeten 500ml Braunglasflasche.
https://www.gebindor.de/flaschen/glasflaschen/meplatflasche/7311/500-ml-meplatflasche-glas-braun-pp-28-meplat
Das Produkt wird sowohl beim Tier als auch beim Menschen angewendet.
Die Form des Etiketts muss nicht zwingend der Flaschenform entsprechen.
Beispiele, die uns gut gefallen:
https://www.tulpenkrug.de/collections/limonaden-essencen
https://www.moosquell.bio/vitarel-feldblume-10-kraeuter-ferment-510ml?c=48

```html
<!DOCTYPE html>
<html lang="de">
<head>
<meta charset="utf-8">
<title>Kolloidales Silber – Etikett Vorder- und Rückseite</title>
<link href="https://fonts.googleapis.com/css2?family=Dosis:wght@600&family=Oswald:wght@300;400&family=Caveat+Brush&display=swap" rel="stylesheet">
<style>
  :root {
    --canvas: #ffffff;
    --paper-light: #f3f1e6;
    --paper-mid: #e6e2d0;
    --paper-edge: #d2cbb1;
    --brand-green: #6f8a5a;
    --swoosh-teal: #6fb5a6;
    --swoosh-green: #6a8550;
    --silver: #8c8c8c;
    --text: #4f5a3e;
    --badge-green: #3f9a3a;
  }
  * { box-sizing: border-box; margin: 0; padding: 0; }
  html, body { width: 1110px; height: 1200px; overflow: hidden; background: var(--canvas); }
  .sheet { position: relative; width: 1110px; height: 1200px; }

  .label {
    position: absolute; top: 50px; width: 420px; height: 1100px;
    border-radius: 210px 210px 0 0;
    background: radial-gradient(ellipse at 50% 45%, var(--paper-light) 0%, var(--paper-mid) 70%, var(--paper-edge) 100%);
    color: var(--text);
    font-family: "Oswald", sans-serif; font-weight: 300;
    overflow: hidden;
  }
  .label--front { left: 115px; }
  .label--back { left: 575px; }

  .brand {
    position: absolute; top: 240px; left: 0; width: 100%;
    display: flex; align-items: center; justify-content: center; gap: 12px;
    font-family: "Dosis", sans-serif; font-weight: 600; font-size: 36px;
    letter-spacing: 3px; color: var(--brand-green);
  }
  .brand__dot { width: 14px; height: 14px; border-radius: 50%; background: var(--brand-green); }

  .swoosh { position: absolute; top: 355px; left: 0; width: 420px; height: 320px; }

  .product { position: absolute; left: 58px; top: 430px; color: var(--silver); font-family: "Caveat Brush", cursive; }
  .product__line1 { font-size: 56px; line-height: 1; }
  .product__line2 { font-size: 112px; line-height: 1; margin-left: 36px; }

  .uses { position: absolute; left: 38px; top: 780px; width: 350px; }
  .section-title { font-size: 21px; font-weight: 400; margin-bottom: 8px; }
  .uses ul { list-style: none; font-size: 16px; line-height: 1.38; }
  .uses li { position: relative; padding-left: 18px; }
  .uses li::before { content: ""; position: absolute; left: 3px; top: 9px; width: 5px; height: 5px; border-radius: 50%; background: var(--text); }

  .volume { position: absolute; right: 28px; bottom: 18px; font-size: 18px; font-weight: 400; }

  .info { position: absolute; left: 36px; width: 350px; font-size: 16px; line-height: 1.35; }
  .info .section-title { margin-bottom: 2px; }
  .info--ingredients { top: 470px; }
  .info--storage { top: 560px; }
  .info--note { top: 745px; }
  .info--maker { top: 820px; width: 250px; }
  .info--concentration { top: 955px; }
  .info--lot { top: 1010px; }

  .checks { display: flex; gap: 18px; }
  .check { display: flex; align-items: center; gap: 3px; }
  .check__box { width: 12px; height: 12px; border: 1.5px solid var(--text); }

  .badge { position: absolute; right: 32px; }
  .badge--vegan { top: 720px; width: 62px; height: 62px; border-radius: 50%; border: 4px solid var(--badge-green); }
  .badge--cruelty { top: 815px; width: 62px; height: 62px; border-radius: 8px; background: var(--badge-green); opacity: .85; }
</style>
</head>
<body>
<main class="sheet">

  <section class="label label--front" aria-label="Etikett Vorderseite">
    <div class="brand"><span class="brand__dot"></span>KRÄUTERWINKL</div>
    <svg class="swoosh" viewBox="0 0 420 320" aria-hidden="true">
      <path d="M0 120 C 90 20, 300 10, 390 170" fill="none" stroke="var(--swoosh-green)" stroke-width="16" stroke-linecap="round"/>
      <path d="M60 70 C 200 20, 340 60, 400 160 C 415 210, 405 260, 380 300" fill="none" stroke="var(--swoosh-teal)" stroke-width="7" stroke-linecap="round"/>
    </svg>
    <div class="product">
      <div class="product__line1">Kolloidales</div>
      <div class="product__line2">Silber</div>
    </div>
    <div class="uses">
      <p class="section-title">Anwendungsbeispiele:</p>
      <ul>
        <li>Auge: Bindehautentzündung, Gerstenkorn</li>
        <li>Nase: eitrige Sinusitis, Heuschnupfen als Nasenspray</li>
        <li>Mund und Rachen: Halsentzündung, Zahnfleisch­entzündung, Lippenherpes</li>
        <li>Magen-Darm: Magengeschwüre, Sodbrennen, Candida albicans</li>
        <li>Stärkung des Immunsystems</li>
        <li>Fuß- und Hautpilz</li>
        <li>Allergien</li>
        <li>Neurodermitis</li>
      </ul>
    </div>
    <p class="volume">500 ml</p>
  </section>

  <section class="label label--back" aria-label="Etikett Rückseite">
    <div class="brand"><span class="brand__dot"></span>KRÄUTERWINKL</div>
    <svg class="swoosh" viewBox="0 0 420 320" aria-hidden="true">
      <path d="M0 120 C 90 20, 300 10, 390 170" fill="none" stroke="var(--swoosh-green)" stroke-width="16" stroke-linecap="round"/>
      <path d="M60 70 C 200 20, 340 60, 400 160 C 415 210, 405 260, 380 300" fill="none" stroke="var(--swoosh-teal)" stroke-width="7" stroke-linecap="round"/>
    </svg>
    <div class="info info--ingredients">
      <p class="section-title">Inhaltsstoffe:</p>
      <p>Destilliertes Wasser entmineralisiert,<br>Feinsilber Reinheit &gt; 99,99%</p>
    </div>
    <div class="info info--storage">
      <p class="section-title">Lagerung:</p>
      <p>Bei Zimmertemperatur dunkel und außerhalb der Reichweite von Kindern lagern. Jegliche Nähe zu elektromagnetischen Feldern vermeiden und nicht mit Metall in Verbindung bringen.</p>
      <p style="margin-top:8px">Nach dem Öffnen innerhalb 12 Wochen aufbrauchen.</p>
    </div>
    <div class="info info--note">
      <p class="section-title">Hinweis:</p>
      <p>Kein Lebensmittel</p>
    </div>
    <div class="info info--maker">
      <p>Hergestellt in Deutschland von:<br>Tobias Kern, Mira Lindner GbR<br>info.kraeuterwinkl@postfach.de<br>www.kraeuterwinkl-mensch-tier.de</p>
    </div>
    <span class="badge badge--vegan" role="img" aria-label="Vegan-Siegel"></span>
    <span class="badge badge--cruelty" role="img" aria-label="Siegel ohne Tierversuche"></span>
    <div class="info info--concentration">
      <p class="section-title">Konzentration:</p>
      <div class="checks">
        <span class="check"><span class="check__box"></span>25ppm</span>
        <span class="check"><span class="check__box"></span>50ppm</span>
        <span class="check"><span class="check__box"></span>75ppm</span>
        <span class="check"><span class="check__box"></span>100ppm</span>
      </div>
    </div>
    <p class="info info--lot">Los-Nr. &amp; mind. Haltbar bis:</p>
  </section>

</main>
</body>
</html>
```